BPH Business Card 2018

Brellmore Chiropractic. We have two locations that we want to advertise on the same card. Calderwick OrthoAxis campus address: 3815 Pemberly Dr., Suite 240, Flowood, MS 39587. Madison address: 426 Larkmoor Dr., Building D., Madison, MS 39674. website: www.drbrellmore.example. o:(601)555-0148 f:(601)555-0173

Target Market(s)

Health care decision makers: primary care doctors and mothers

Contact Information for Business Card

I have no idea; up for any suggestions and I'd do much better picking from examples versus describing what I'm looking for. We are in a very high end location and would like the cards to look really sharp.

Requirements
Must have
• My name, Tobias R Venmark, D.C.

```html
<!DOCTYPE html>
<html lang="en">
<head>
<meta charset="utf-8">
<title>Brellmore Chiropractic Business Card</title>
<link rel="stylesheet" href="https://fonts.googleapis.com/css2?family=Roboto:wght@400&family=Roboto+Condensed:wght@400;700&display=swap">
<style>
  :root {
    --backdrop: #e8e5e1;
    --card-dark: #232323;
    --card-light: #f3f3f3;
    --figure-tone: #f1f1f1;
    --text-light: #ffffff;
    --text-dark: #1c1c1c;
    --text-muted: #555555;
    --shadow: rgba(0, 0, 0, 0.28);
  }
  html, body {
    margin: 0;
    padding: 0;
    width: 1200px;
    height: 960px;
    overflow: hidden;
    background: var(--backdrop);
  }
  .canvas {
    position: relative;
    width: 1200px;
    height: 960px;
  }
  .card {
    position: absolute;
    box-shadow: 0 3px 8px var(--shadow);
    overflow: hidden;
  }
  .card-front {
    left: 314px;
    top: 113px;
    width: 600px;
    height: 343px;
    background: var(--card-dark);
    color: var(--text-light);
    font-family: "Roboto", Arial, sans-serif;
  }
  .card-back {
    left: 312px;
    top: 472px;
    width: 598px;
    height: 343px;
    background: var(--card-light);
  }
  .figure-area {
    position: absolute;
    right: 0;
    top: 0;
    width: 320px;
    height: 343px;
  }
  .doctor-name {
    position: absolute;
    left: 36px;
    top: 46px;
    margin: 0;
    font-family: "Roboto Condensed", "Arial Narrow", sans-serif;
    font-weight: 700;
    font-size: 21px;
    letter-spacing: 0.2px;
  }
  .locations {
    position: absolute;
    left: 35px;
    top: 121px;
    font-size: 14px;
    line-height: 18px;
  }
  .location {
    margin: 0 0 6px;
    font-style: normal;
  }
  .contact-list {
    position: absolute;
    left: 35px;
    top: 246px;
    margin: 0;
    padding: 0;
    list-style: none;
    font-size: 14px;
    line-height: 19px;
  }
  .contact-item {
    display: flex;
    align-items: center;
    gap: 8px;
  }
  .contact-icon {
    width: 14px;
    height: 14px;
    fill: var(--text-light);
  }
  .brand-name {
    position: absolute;
    left: 0;
    right: 0;
    top: 130px;
    margin: 0;
    text-align: center;
    font-family: "Roboto Condensed", "Arial Narrow", sans-serif;
    font-weight: 400;
    font-size: 40px;
    letter-spacing: 1px;
    color: var(--text-dark);
  }
  .brand-web {
    position: absolute;
    left: 0;
    right: 0;
    top: 281px;
    margin: 0;
    text-align: center;
    font-family: "Roboto", Arial, sans-serif;
    font-size: 15px;
    letter-spacing: 5px;
    color: var(--text-muted);
  }
</style>
</head>
<body>
<main class="canvas">
  <section class="card card-front">
    <svg class="figure-area" viewBox="0 0 320 343" role="img" aria-label="Line illustration of a reaching human torso, light on dark">
      <path d="M320 0 L320 343 L0 343 C40 300 50 240 70 190 C80 120 70 60 110 30 C150 5 200 60 240 40 C270 25 290 10 305 0 Z" fill="var(--figure-tone)"/>
    </svg>

    <h1 class="doctor-name">TOBIAS R VENMARK, D.C.</h1>

    <div class="locations">
      <address class="location">Calderwick OrthoAxis campus :<br>3815 Pemberly Dr., Suite 240<br>Flowood, MS 39587.</address>
      <address class="location">Madison address:<br>426 Larkmoor Dr., Building D.<br>Madison, MS 39674.</address>
    </div>

    <ul class="contact-list">
      <li class="contact-item">
        <svg class="contact-icon" viewBox="0 0 16 16" aria-hidden="true"><path d="M3.5 1 L6 1 L7 4.5 L5.3 5.7 C6.2 7.8 8.2 9.8 10.3 10.7 L11.5 9 L15 10 L15 12.5 C15 13.9 13.9 15 12.5 15 C6.7 15 1 9.3 1 3.5 C1 2.1 2.1 1 3.5 1 Z"/></svg>
        <span>(601)555-0148</span>
      </li>
      <li class="contact-item">
        <svg class="contact-icon" viewBox="0 0 16 16" aria-hidden="true"><path d="M4 1 H12 V5 H4 Z M1 6 H15 V12 H12 V10 H4 V12 H1 Z M5 11 H11 V15 H5 Z"/></svg>
        <span>(601)555-0173</span>
      </li>
      <li class="contact-item">
        <svg class="contact-icon" viewBox="0 0 16 16" aria-hidden="true"><circle cx="8" cy="8" r="7"/><path d="M4 5 C6 4 7 6 6 8 C5 10 7 11 7 13 M10 3 C9 5 11 6 12 7 C13 8 12 10 11 11" stroke="var(--card-dark)" stroke-width="1.3" fill="none"/></svg>
        <span>www.drbrellmore.example</span>
      </li>
    </ul>
  </section>

  <section class="card card-back">
    <p class="brand-name">BRELLMORE CHIROPRACTIC</p>
    <p class="brand-web">WWW.DRBRELLMORE.EXAMPLE</p>
  </section>
</main>
</body>
</html>
```